TLR Property - Business Cards

Looking for a business card & general letterhead, signage etc design for our new logo.

Colours:
000a20
0056a2
00b5ef
0088ce
68cef2

Fonts:
Poppins
Karla

Please keep look and feel of new brand - example in the zip package I sent.

```html
<!DOCTYPE html>
<html lang="en">
<head>
<meta charset="utf-8">
<title>TLR Property – Business Cards</title>
<link rel="stylesheet" href="https://fonts.googleapis.com/css2?family=Poppins:wght@400;600;700&display=swap">
<style>
  :root {
    --ink: #000a20;
    --brand-blue: #0056a2;
    --sky: #00b5ef;
    --mid-blue: #0088ce;
    --pale-blue: #68cef2;
    --white: #ffffff;
    --stage: #1c1c1e;
  }
  * { box-sizing: border-box; margin: 0; padding: 0; }
  html, body { width: 1200px; height: 1015px; overflow: hidden; }
  body {
    background: var(--stage);
    font-family: "Poppins", sans-serif;
    position: relative;
  }
  .card {
    position: absolute;
    left: 290px;
    width: 620px;
    height: 354px;
    overflow: hidden;
  }
  .card--front { top: 110px; background: var(--brand-blue); }
  .card--back { top: 550px; background: var(--white); }

  .wordmark {
    display: flex;
    align-items: center;
    gap: 16px;
    font-weight: 700;
    letter-spacing: 0.5px;
    white-space: nowrap;
  }
  .wordmark__dot {
    width: 44px; height: 44px; border-radius: 50%;
    background: var(--pale-blue);
    flex: none;
  }
  .card--front .wordmark {
    position: absolute; inset: 0; justify-content: center;
    color: var(--white); font-size: 50px;
  }
  .card--back .wordmark {
    position: absolute; left: 30px; top: 152px;
    color: var(--brand-blue); font-size: 30px; gap: 12px;
  }
  .card--back .wordmark__dot { width: 30px; height: 30px; }

  .back__panel {
    position: absolute; left: 0; top: 0; width: 620px; height: 354px;
  }
  .contact {
    position: absolute; left: 352px; top: 44px; width: 250px;
    color: var(--white);
  }
  .contact__name { font-size: 19px; font-weight: 700; line-height: 1.1; }
  .contact__role { font-size: 13px; font-weight: 400; margin-top: 2px; }
  .contact__rule { width: 56px; height: 1px; background: var(--white); opacity: .8; margin: 18px 0 16px; }
  .contact__list { list-style: none; font-size: 13px; line-height: 1.75; }
  .contact__list li { display: flex; align-items: center; gap: 9px; white-space: nowrap; }
  .contact__list svg { width: 13px; height: 13px; flex: none; }
  .contact__address { font-size: 13px; line-height: 1.45; white-space: nowrap; }
</style>
</head>
<body>
  <section class="card card--front" aria-label="Business card front">
    <div class="wordmark"><span class="wordmark__dot"></span>TLR Property</div>
  </section>

  <section class="card card--back" aria-label="Business card back">
    <svg class="back__panel" viewBox="0 0 620 354" aria-hidden="true">
      <polygon points="232,0 262,0 322,60 322,84" fill="var(--sky)"/>
      <polygon points="250,0 280,0 322,44 322,70" fill="var(--pale-blue)"/>
      <polygon points="268,0 300,0 322,26 322,54" fill="var(--mid-blue)"/>
      <rect x="322" y="0" width="298" height="354" fill="var(--brand-blue)"/>
    </svg>
    <div class="wordmark"><span class="wordmark__dot"></span>TLR Property</div>
    <div class="contact">
      <p class="contact__name">MARCUS ELLERY</p>
      <p class="contact__role">Managing Director</p>
      <div class="contact__rule"></div>
      <ul class="contact__list">
        <li><svg viewBox="0 0 16 16"><path d="M4 1l3 3-2 2c1 2 3 4 5 5l2-2 3 3-2 3C7 15 1 9 1 3z" fill="var(--white)"/></svg>055-210 384 617</li>
        <li><svg viewBox="0 0 16 16"><rect x="1" y="3" width="14" height="10" fill="none" stroke="var(--white)" stroke-width="1.5"/><path d="M1 3l7 6 7-6" fill="none" stroke="var(--white)" stroke-width="1.5"/></svg>hello@tlrhomes.com</li>
        <li><svg viewBox="0 0 16 16"><circle cx="8" cy="8" r="6.5" fill="none" stroke="var(--white)" stroke-width="1.4"/><ellipse cx="8" cy="8" rx="3" ry="6.5" fill="none" stroke="var(--white)" stroke-width="1.2"/><path d="M1.5 8h13" stroke="var(--white)" stroke-width="1.2"/></svg>www.tlrhomes.com</li>
      </ul>
      <div class="contact__rule"></div>
      <p class="contact__address">18, Harbour View Lane<br>30917, Northland</p>
    </div>
  </section>
</body>
</html>
```